CareVantRx business cards

We need a business card design that we could customize as needed for employees. We will need space for Name, Title, 1-2 phone numbers and email address.

We are a Pharmacy Benefits Management (PBM) company for hospice agencies and beginning a nationwide expansion. Attached is a vector file of our logo.

Cards can be single or double sided.

Industry/Entity Type

Business

```html
<!DOCTYPE html>
<html lang="en">
<head>
<meta charset="utf-8">
<title>CareVantRx Business Card</title>
<link rel="stylesheet" href="https://fonts.googleapis.com/css2?family=Michroma&family=Archivo+Black&display=swap">
<style>
  :root {
    --card-blue: #0090dc;
    --card-edge: #2b6ea6;
    --ink-navy: #1b1f7a;
    --brand-blue: #1e3f8f;
    --label-white: #ffffff;
    --mark-fade: rgba(30, 63, 143, 0.20);
  }
  * { margin: 0; padding: 0; box-sizing: border-box; }
  html, body {
    width: 1200px;
    height: 733px;
    overflow: hidden;
    background: var(--card-blue);
  }
  .card {
    position: relative;
    width: 1200px;
    height: 733px;
    background: var(--card-blue);
    overflow: hidden;
    font-family: "Michroma", sans-serif;
    color: var(--label-white);
  }
  .card-frame {
    position: absolute;
    inset: 0;
    border: 2px solid var(--card-edge);
    pointer-events: none;
    z-index: 3;
  }
  .corner-mark {
    position: absolute;
    left: 808px;
    top: 292px;
    width: 470px;
    height: 470px;
    border-radius: 72px;
    background: linear-gradient(160deg, var(--mark-fade), rgba(30, 63, 143, 0.05));
  }
  .brand-square {
    position: absolute;
    left: 120px;
    top: 47px;
    width: 151px;
    height: 152px;
    border-radius: 16px;
    background: var(--brand-blue);
  }
  .brand-name {
    position: absolute;
    left: 316px;
    top: 60px;
    width: 760px;
    height: 130px;
    overflow: visible;
  }
  .brand-name text {
    font-family: "Archivo Black", sans-serif;
    font-size: 122px;
    fill: var(--brand-blue);
  }
  .label {
    position: absolute;
    font-size: 14px;
    font-variant: small-caps;
    letter-spacing: 1.5px;
    line-height: 1;
    white-space: nowrap;
  }
  .label-title { left: 376px; top: 210px; }
  .label-name { left: 600px; top: 400px; transform: translateX(-50%); }
  .label-phone { left: 600px; top: 451px; transform: translateX(-50%); }
  .label-office { left: 88px; top: 579px; }
  .label-email { left: 672px; top: 579px; }
  .name-rule {
    position: absolute;
    left: 314px;
    top: 432px;
    width: 569px;
    height: 4px;
    background: var(--ink-navy);
  }
  .column-divider {
    position: absolute;
    left: 594px;
    top: 565px;
    width: 8px;
    height: 166px;
    background: var(--ink-navy);
  }
</style>
</head>
<body>
  <div class="card">
    <div class="corner-mark" aria-hidden="true"></div>

    <div class="brand-square" aria-hidden="true"></div>
    <svg class="brand-name" viewBox="0 0 760 130" role="img" aria-label="CareVantRx">
      <text x="0" y="114" textLength="756" lengthAdjust="spacing">CareVantRx</text>
    </svg>

    <span class="label label-title">Title</span>
    <span class="label label-name">Name</span>
    <div class="name-rule" aria-hidden="true"></div>
    <span class="label label-phone">Telp</span>

    <span class="label label-office">Office :</span>
    <div class="column-divider" aria-hidden="true"></div>
    <span class="label label-email">E-mail :</span>

    <div class="card-frame" aria-hidden="true"></div>
  </div>
</body>
</html>
```